We need to a website for a contact center that provides answering services by voice and chat.

A similar website in terms of design is the following site:
http://www.brindlequay.example/

The colors and look and feel should be different and creative but the structure should be similar to the above mentioned website.

Attached is the text file.

The design should communicate professionalism and friendly customer service oriented company. The visitor to the site must have a feel that "this company looks professional and they will take care of my client."

I am looking for design only, but if the designer will also do the coding, it will be an advantage.

Target Market(s)

Our target market are lawyers and doctors who require someone to answer their clients calls 24/7.

Industry/Entity Type

It Company

Requirements
Nice to have
• Since the company is based in Dubai, the website should reflect the Middle East people not pure European or pure Asians. A mixture of nationalities is fine to be visible in the pictures but it must include at least an arab or middle eastern person.
Should not have
• No old style, Times Roman font, do not include illustrations or cartoon graphics or pictures that are very common or widely used.

```html
<!DOCTYPE html>
<html lang="en">
<head>
<meta charset="utf-8">
<title>Larkfield Group – Premium Live Receptionist</title>
<link href="https://fonts.googleapis.com/css2?family=Open+Sans:wght@400;600;700&display=swap" rel="stylesheet">
<style>
:root{
  --page:#f5f5f5;
  --white:#ffffff;
  --ink:#222222;
  --body:#555555;
  --brand:#8e1c1c;
  --button:#b8100f;
  --hero:#333333;
  --footer:#363636;
  --footer-deep:#1e1e1e;
  --footer-text:#a8a8a8;
  --rule:#dddddd;
}
*{box-sizing:border-box;margin:0;padding:0}
html,body{width:1109px;height:1200px;overflow:hidden;background:var(--page);font-family:'Open Sans',sans-serif;color:var(--body)}
.site{position:absolute;left:92px;top:0;width:925px;height:1200px;background:var(--white);overflow:hidden}
a{color:inherit}

/* header */
.brand{position:absolute;left:22px;top:14px;color:var(--ink);font-weight:400;line-height:1}
.brand-name{font-size:33px;letter-spacing:1px}
.brand-sub{font-size:13px;letter-spacing:11px;margin-top:6px}
.topbar{position:absolute;right:20px;top:9px;display:flex;align-items:center;gap:14px;font-size:14.5px}
.topbar .login{color:var(--ink)}
.topbar .price{color:var(--brand)}
.topbar .phone{background:var(--hero);color:var(--white);font-weight:600;font-size:21px;padding:0 8px;height:30px;line-height:30px}
.nav{position:absolute;right:20px;top:67px;display:flex;gap:5px;font-size:12px;color:var(--ink)}
.nav span{padding:2px 8px;border-radius:2px}
.nav .active{background:var(--button);color:var(--white)}

/* hero */
.hero{position:absolute;left:0;top:96px;width:925px;height:274px;background:var(--hero)}
.hero-photo{position:absolute;left:21px;top:29px;width:431px;height:211px;border:1px solid #666;
  background:linear-gradient(100deg,#d9dde2 0%,#bfc6cf 40%,#9aa4ae 70%,#c9ced4 100%)}
.hero-title{position:absolute;left:473px;top:26px;color:var(--white);font-weight:700;font-size:31px;white-space:nowrap;line-height:1.2}
.hero-sub{position:absolute;left:475px;top:70px;color:var(--white);font-size:20px;white-space:nowrap}
.hero-copy{position:absolute;left:477px;top:104px;width:410px;color:#eeeeee;font-size:11.6px;line-height:15.5px}
.signup{position:absolute;left:479px;top:168px;width:424px;height:72px;border:1px solid #666;border-radius:3px}
.field{position:absolute;background:var(--white);border:1px solid #bbb;height:25px;font-size:11.5px;color:#999;padding:4px 8px}
.go-btn{position:absolute;background:var(--button);color:var(--white);font-size:13px;text-align:center;border:1px solid #ddd}

/* features */
.features{position:absolute;left:22px;top:393px;width:882px;display:flex;justify-content:space-between;font-size:20px;color:#444}
.feature{display:flex;align-items:center;gap:14px}

/* content */
.h2{color:var(--brand);font-size:18px;font-weight:400}
.welcome{position:absolute;left:22px;top:457px;width:490px}
.welcome p{font-size:11.6px;line-height:21.3px;margin-top:12px}
.welcome p + p{margin-top:21px}
.welcome .more{display:block;margin-top:22px;color:var(--brand);font-size:12px}
.divider{position:absolute;left:526px;top:460px;width:1px;height:307px;background:var(--rule)}
.benefits{position:absolute;left:561px;top:457px;width:350px}
.benefits ul{list-style:none;margin-top:13px}
.benefits li{position:relative;font-size:11.6px;line-height:21.7px;color:var(--ink);text-decoration:underline}
.benefits li.ar::before{content:"›";position:absolute;left:-20px;color:var(--brand);font-weight:700;text-decoration:none;font-size:15px}
.service{position:absolute;left:22px;top:796px;width:890px}
.service p{font-size:11.6px;line-height:21.3px;margin-top:13px}

/* footer */
.footer{position:absolute;left:0;top:932px;width:925px;height:214px;background:var(--footer)}
.footer h3{color:var(--white);font-weight:400;font-size:17px}
.about{position:absolute;left:24px;top:27px;width:480px}
.about p{color:var(--footer-text);font-size:11.6px;line-height:22.6px;margin-top:8px}
.newsletter{position:absolute;left:562px;top:27px;width:345px}
.news-input{position:absolute;left:-3px;top:37px;width:282px;height:31px;background:var(--white);border:1px solid #999}
.news-go{position:absolute;left:290px;top:37px;width:55px;height:31px;background:var(--white);border:2px solid #222;text-align:center;color:#333;font-size:16px;line-height:27px}
.connected{position:absolute;left:0;top:128px}
.social{display:flex;gap:7px;margin-top:14px}
.social i{width:20px;height:20px;border-radius:50%;background:#555;border:1px solid #666;display:block}
.bottom{position:absolute;left:0;top:1146px;width:925px;height:54px;background:var(--footer-deep);color:#aaa;font-size:12.5px;display:flex;align-items:center;justify-content:space-between;padding:0 25px 0 22px}
.bottom .links span{margin:0 9px;color:#777}
</style>
</head>
<body>
<div class="site">
  <header>
    <div class="brand"><div class="brand-name">LARKFIELD</div><div class="brand-sub">GROUP</div></div>
    <div class="topbar"><span class="login">Client Login</span><span class="price">From $2.66 A day</span><span class="phone">+123 456 78.90.000</span></div>
    <nav class="nav"><span class="active">Home</span><span>How It Works</span><span>Industries</span><span>About Us</span><span>Testimonials</span><span>Pricing</span><span>Press Room</span><span>Contact Us</span></nav>
  </header>

  <section class="hero">
    <div class="hero-photo" role="img" aria-label="Team of smiling receptionists wearing headsets in a bright office"></div>
    <h1 class="hero-title">Premium Live Receptionist.</h1>
    <div class="hero-sub">Route Your Businees Calls to Any Location.</div>
    <p class="hero-copy">Lorem Ipsum is simply dummy text of the printing and typesetting industry. Lorem Ipsum has been the industry's standard dummy text ever since the when an unknown printer.</p>
    <div class="signup">
      <div class="field" style="left:8px;top:8px;width:200px">Name</div>
      <div class="field" style="left:214px;top:8px;width:200px">Phone</div>
      <div class="field" style="left:8px;top:40px;width:310px">Email</div>
      <div class="go-btn" style="left:326px;top:40px;width:88px;height:25px;line-height:23px">Get Started</div>
    </div>
  </section>

  <section class="features">
    <div class="feature">
      <svg width="38" height="32" viewBox="0 0 38 32"><path d="M2 11h7l9-8v26l-9-8H2z" fill="#222"/><path d="M23 10q4 6 0 12M27 6q7 10 0 20M31 3q9 13 0 26" stroke="#222" stroke-width="2.5" fill="none"/></svg>
      <span>Listen to a Live Demo</span>
    </div>
    <div class="feature">
      <svg width="38" height="34" viewBox="0 0 38 34"><rect x="3" y="5" width="24" height="26" fill="none" stroke="#222" stroke-width="3"/><path d="M8 13h12M8 19h10M8 25h8" stroke="#222" stroke-width="2.5"/><path d="M20 24l14-16 3 3-14 16-5 2z" fill="#222"/></svg>
      <span>Request Pricing</span>
    </div>
    <div class="feature">
      <svg width="36" height="38" viewBox="0 0 36 38"><ellipse cx="18" cy="24" rx="12" ry="12" fill="#222"/><path d="M10 4q10-4 14 6" stroke="#222" stroke-width="3" fill="none"/><circle cx="15" cy="20" r="4" fill="#fff"/></svg>
      <span>Online Signup</span>
    </div>
  </section>

  <section class="welcome">
    <h2 class="h2">Welcome to Larkfield Group</h2>
    <p>Lorem Ipsum is simply dummy text of the printing and typesetting industry. Lorem Ipsum has been the industry's standard dummy text ever since the 1500s, when an unknown printer took a galley of type and scrambled it to make a type specimen book.</p>
    <p>It has survived not only five centuries, but also the leap into electronic typesetting, remaining essentially unchanged. It was popularised in the 1960s with the release of Letraset sheets containing Lorem Ipsum passages.</p>
    <p>Lorem Ipsum is simply dummy text of the printing and typesetting industry stry's standard dummy text ever since the 1500s, when an unknown printer took a galley of type and scrambled it to make a type specimen book.</p>
    <a class="more" href="#">Read More</a>
  </section>
  <div class="divider"></div>
  <section class="benefits">
    <h2 class="h2">Top Ten Ways Your Company Can Benefit</h2>
    <ul>
      <li class="ar">Capture more business &amp; increase profits.</li>
      <li>Save thousands on labor costs.</li>
      <li class="ar">Improve your company's "phone image".</li>
      <li>Streamline your call flow.</li>
      <li class="ar">Conduct business 24/7 without the overhead.</li>
      <li class="ar">Take advantage of a turn-key, streamlined solution.</li>
      <li class="ar">Respond instantaneously to clients and prospects.</li>
      <li class="ar">Brindle Quay Network uses the most reliable equipment in the industry.</li>
      <li class="ar">Brindle Quay Network selects the right people with the best voices.</li>
      <li class="ar">Brindle Quay Network over-staffs receptionists to minimize hold times.</li>
    </ul>
  </section>

  <section class="service">
    <h2 class="h2">24/7 Live Receptionist &amp; Answering Service</h2>
    <p>Lorem Ipsum is simply dummy text of the printing and typesetting industry. Lorem Ipsum has been the industry's standard dummy text ever since the 1500s, when an unknown printer took a galley of type and scrambled it to make a type specimen book It has survived not only five centuries, but also the leap into electronic typesetting, remaining essentially unchanged. It was popularised in the 1960s with the release of Letraset sheets containing Lorem Ipsum passages.</p>
  </section>

  <footer class="footer">
    <div class="about">
      <h3>About Us</h3>
      <p>Larkfield Group Network is a U.S.-based 24/7/365 business call center and live answering service that provides customized live receptionist solutions for small, medium, and large businesses nationally. Inbound call center services include 24-hour off-site live U.S. receptionists who will answer business phones even during non-business hours (such as 24-hour emergency dispatch service). Live remote office receptionists answer your office phone line and deliver your messages.</p>
    </div>
    <div class="newsletter">
      <h3>Sign up for our Free Monthly Newsletter</h3>
      <div class="news-input"></div>
      <div class="news-go">Go</div>
      <div class="connected">
        <h3>Keeping You Connected</h3>
        <div class="social"><i></i><i></i><i></i><i></i><i></i><i></i><i></i></div>
      </div>
    </div>
  </footer>
  <div class="bottom">
    <div class="links">Sitemap<span>|</span>Privacy<span>|</span>Terms &amp; Conditions</div>
    <div>©2013 Larkfield Group Network</div>
  </div>
</div>
</body>
</html>
```